pet minder needs a flyer design

I need a flyer design for my pet minding/ dog walking business.
My business is called 'Muddy paws happy tail crew', i would like the business
name included in on the flyer (i dont mind how big or small it is)
i was hoping for a design that was warm and friendly and obviously
incorporates animals :)
I have attached the information i would like included on the flyer below

Target Market(s)

all ages.

Industry/Entity Type

Pet Care

Font styles to use
Serif

Colors
ec1f27

Requirements
Must have
• information about the services i provide
• incorporates animals
Nice to have
• colour red

```html
<!DOCTYPE html>
<html lang="en">
<head>
<meta charset="utf-8">
<title>Petsitter Flyer</title>
<link href="https://fonts.googleapis.com/css2?family=Arimo:wght@400;700&display=swap" rel="stylesheet">
<style>
  :root {
    --frame: #3a2116;
    --red: #e31b23;
    --yellow: #ffc20e;
    --white: #ffffff;
    --ink: #2a2a2a;
    --footer-bg: #ececec;
    --photo-light: #f7f5f3;
    --photo-mid: #e4dcd4;
  }
  * { box-sizing: border-box; margin: 0; padding: 0; }
  html, body { width: 861px; height: 1200px; overflow: hidden; background: var(--frame); }
  .flyer {
    position: absolute; left: 22px; top: 22px; width: 817px; height: 1156px;
    background: var(--white); overflow: hidden;
    font-family: "Arimo", Arial, sans-serif;
  }
  .photo {
    position: absolute; left: 400px; top: 40px; width: 417px; height: 800px;
    background: radial-gradient(ellipse at 60% 55%, var(--photo-mid) 0%, var(--photo-light) 60%, var(--white) 100%);
  }
  .headline-band {
    position: absolute; left: 0; top: 12px; width: 600px; height: 190px;
  }
  .headline {
    position: absolute; left: 30px; top: 26px;
    color: var(--white); font-weight: 700; font-size: 64px; line-height: 74px;
  }
  .pitch {
    position: absolute; left: 18px; top: 345px; width: 420px;
    color: var(--red); font-weight: 700; font-size: 37px; line-height: 50px;
    text-align: center;
  }
  .services-tab {
    position: absolute; left: 0; top: 838px; width: 360px; height: 52px;
  }
  .services-tab span {
    position: absolute; left: 28px; top: 9px;
    color: var(--ink); font-weight: 700; font-size: 32px;
  }
  .services {
    position: absolute; left: 0; top: 885px; width: 817px; height: 158px;
    background: var(--red);
  }
  .service {
    position: absolute; display: flex; align-items: center; gap: 10px;
    color: var(--white); font-size: 31px;
  }
  .paw { width: 30px; height: 30px; fill: var(--yellow); flex: none; }
  .contact {
    position: absolute; left: 0; top: 1053px; width: 817px; height: 92px;
    background: var(--footer-bg);
    display: flex; align-items: center; justify-content: center;
    font-size: 41px; color: var(--ink);
  }
  .contact .name { color: var(--red); margin-left: 12px; }
  .contact .phone { margin-left: 12px; }
</style>
</head>
<body>
<svg width="0" height="0" style="position:absolute">
  <defs>
    <symbol id="paw" viewBox="0 0 30 30">
      <ellipse cx="15" cy="21" rx="7.5" ry="6.5"/>
      <ellipse cx="5" cy="13" rx="3" ry="4"/>
      <ellipse cx="11" cy="7" rx="3" ry="4"/>
      <ellipse cx="19" cy="7" rx="3" ry="4"/>
      <ellipse cx="25" cy="13" rx="3" ry="4"/>
    </symbol>
  </defs>
</svg>

<main class="flyer">
  <div class="photo" role="img" aria-label="Photo of a woman in a red top holding a lead while a bulldog stands up on its hind legs"></div>

  <svg class="headline-band" viewBox="0 0 600 190" aria-hidden="true">
    <polygon points="0,0 600,0 520,190 0,190" fill="var(--red)"/>
  </svg>
  <h1 class="headline">Do you need<br>a petsitter?</h1>

  <p class="pitch">I am a fully qualified veterinary nurse who will look after your animals like they were my own own, when you go away!</p>

  <div class="services-tab">
    <svg width="360" height="52" viewBox="0 0 360 52" aria-hidden="true">
      <polygon points="0,0 340,0 360,52 0,52" fill="var(--yellow)"/>
    </svg>
    <span>Services Provide</span>
  </div>

  <section class="services">
    <div class="service" style="left:30px; top:32px"><svg class="paw"><use href="#paw"/></svg>Pet Minding</div>
    <div class="service" style="left:292px; top:32px"><svg class="paw"><use href="#paw"/></svg>House Sitting</div>
    <div class="service" style="left:557px; top:32px"><svg class="paw"><use href="#paw"/></svg>Dog Walking</div>
    <div class="service" style="left:30px; top:94px"><svg class="paw"><use href="#paw"/></svg>Medication</div>
    <div class="service" style="left:292px; top:94px"><svg class="paw"><use href="#paw"/></svg>Collecting Mail/Watering Plants</div>
  </section>

  <footer class="contact">
    enquire call me:<span class="name">Jenna</span><span class="phone">0400 123 987</span>
  </footer>
</main>
</body>
</html>
```